Stationery Design Project

Logo is already created , rest of stationary should reflect the below.
we work on the field of Oil and Gas - providing equipment and rental tools.
we want to communicate the below
1- sharp approach , 24/7 available.
2- we track our documents and value our internal process.
3- HSE , health and safety is our DNA.
contacts
Q Ventures for rental tools and equipment
Office 5, 12th floor, amber crest tower, Marlow Quay, Abu Dhabi
Mob.050 847 3062 /phone.02-418 5927

Target Market(s)

Oil and Gas engineers and Operation Managers.

Industry/Entity Type

Health

Font styles to use
Serif

Colors
0592cd
33a6d7
86cae6
86cfc6
add136

Requirements
Must have
• must have 6 pages , use all materials we supply.
Nice to have
• Tag every page with ZERO DISCHARGE
reflect responsibility to environment.
Should not have
• complicated fonts should not be used.

```html
<!DOCTYPE html>
<html lang="en">
<head>
<meta charset="utf-8">
<title>Q Ventures Stationery</title>
<link rel="stylesheet" href="https://fonts.googleapis.com/css2?family=Source+Sans+3:wght@400;600;700&family=Dancing+Script:wght@600&display=swap">
<style>
  :root {
    --backdrop: #bcbdbf;
    --paper: #ffffff;
    --brand-blue: #0d56a6;
    --brand-grey: #9a9b9d;
    --ink: #1d1d1b;
    --muted: #6a7f95;
    --rule: #6d5a9a;
  }
  * { margin: 0; padding: 0; box-sizing: border-box; }
  html, body { width: 1200px; height: 897px; overflow: hidden; }
  body {
    background: var(--backdrop);
    font-family: "Source Sans 3", Arial, sans-serif;
    color: var(--ink);
    position: relative;
  }
  .sheet {
    position: absolute;
    background: var(--paper);
    box-shadow: 5px 6px 6px rgba(0,0,0,0.35);
    overflow: hidden;
  }
  .brand-mark {
    position: absolute;
    display: flex;
    align-items: center;
    gap: 8px;
    font-weight: 700;
    color: var(--brand-blue);
    letter-spacing: 0.02em;
    white-space: nowrap;
  }
  .brand-dot {
    border-radius: 50%;
    background: var(--brand-grey);
    flex: none;
  }

  /* Letterhead */
  .letterhead { left: 72px; top: 73px; width: 541px; height: 762px; }
  .letterhead .side-band { position: absolute; left: 0; top: 0; width: 78px; height: 100%; background: var(--brand-blue); }
  .letterhead .brand-mark { left: 58px; top: 48px; font-size: 36px; }
  .letterhead .brand-dot { width: 60px; height: 60px; }
  .date-line { position: absolute; left: 104px; top: 182px; font-size: 7px; font-weight: 600; }
  .date-line span { display: inline-block; width: 50px; border-bottom: 1px solid var(--rule); margin-left: 8px; }
  .recipient { position: absolute; left: 104px; top: 205px; }
  .recipient-name { font-size: 10px; font-weight: 700; color: var(--brand-blue); letter-spacing: 0.03em; }
  .recipient-role { font-size: 8.5px; color: var(--muted); margin-top: 1px; }
  .letter-body { position: absolute; left: 104px; top: 247px; width: 405px; font-size: 10.3px; line-height: 12.4px; }
  .letter-body p + p { margin-top: 12.4px; }
  .signature { position: absolute; left: 104px; top: 615px; font-family: "Dancing Script", cursive; font-size: 24px; color: var(--brand-blue); }
  .letter-footer { position: absolute; left: 104px; top: 676px; font-size: 8.3px; }
  .company-line { font-weight: 700; }
  .address-line { margin-top: 4px; }
  .contact-grid { display: grid; grid-template-columns: 82px auto; row-gap: 4px; margin-top: 9px; }
  .contact-item { display: flex; align-items: center; gap: 6px; }
  .contact-item svg { width: 9px; height: 9px; fill: var(--brand-blue); flex: none; }

  /* Envelope back */
  .envelope-back { left: 677px; top: 92px; width: 450px; height: 225px; }
  .envelope-flap { position: absolute; left: 0; top: 0; width: 100%; height: 49px; }
  .envelope-back .brand-mark { left: 147px; top: 11px; font-size: 19px; color: var(--paper); }
  .envelope-back .brand-dot { width: 28px; height: 28px; }

  /* Envelope front */
  .envelope-front { left: 674px; top: 354px; width: 454px; height: 228px; }
  .envelope-front .side-band { position: absolute; left: 0; top: 0; width: 47px; height: 100%; background: var(--brand-blue); }
  .envelope-front .brand-mark { left: 34px; top: 28px; font-size: 20px; }
  .envelope-front .brand-dot { width: 34px; height: 34px; }
  .envelope-address { position: absolute; left: 83px; top: 183px; font-size: 7px; line-height: 9.5px; font-weight: 600; }
</style>
</head>
<body>

<section class="sheet letterhead">
  <div class="side-band"></div>
  <div class="brand-mark"><span class="brand-dot"></span>Q VENTURES</div>

  <div class="date-line">Date<span></span></div>
  <div class="recipient">
    <div class="recipient-name">KARIM NADER</div>
    <div class="recipient-role">President</div>
  </div>

  <div class="letter-body">
    <p>odales semper, nisl in turpis metus nonummy nisl at erat sed condimentum justo sem, lobortis fringilla, massa. Suspendisse est ultricies viverra ligula. Nulla eu diam. Morbi pede Lorem ipsum vel neque ante felis, feugiat dui, eu nunc. Praesent ac lacinia dignissim, sapie vitae dui eu neque placerat nec, hendrerit libero. Cras magna ut leo ultrices urna, pellentesque erat sit amet, est. Aliquam sed turpis. Mauris luctus pellentesque. Praesent gravida gravida elit. Mauris vel risus. Sed vehicula dignissim. Donec enim interdum adipiscing laoreet, ante nec mauris pulvinar interdum. Nulla iaculis pede sed libero malesuada aliquet, purus est, viverra enim enim aliquam</p>
    <p>nunc, lobortis velit nulla facilisis sem id sapien. Donec nonummy gravida. Pellentesque euismod, nulla dolor sit amet, tempor venenatis arcu. Aenean vel nibh. Cras vitae ipsum dolor auctor congue eget, eros. Sed posuere cubilia Curae; Sed eu odio. Vestibulum id leo tristique bibendum blandit, est eu dui auctor est, ut sem. Pellentesque nunc. Nam ipsum. Duis vehicula sit amet quam. Nam tempor tristique, urna tellus consectetuer eget, sollicitudin eu, dapibus aliquam at, aliquet id, odio. Suspendisse potenti. Vestibulum ante eu mauris. Etiam dapibus a, tellus. Quisque rutrum, libero nunc, at tellus. Donec porta, metus nunc, lobortis non, tristique mauris non</p>
    <p>accumsan, urna tellus ante vitae wisi magna, at adipiscing elit. Vestibulum elit sit amet mauris. Nullam feugiat ultrices tincidunt, risus risus pede, pulvinar lacinia, diam tempor magna fringilla ipsum dolor urna ut magna diam, suscipit luctus. Aenean vel ligula dui, ultrices consectetuer. Aliquam rhoncus a, dolor. In lacus diam sit amet, vulputate fringilla. Morbi ut tortor. Cras ut justo. Nam molestie. Vivamus ut orci imperdiet sit amet tellus. Quisque nec egestas sodales, velit non elit at tellus. Fusce ullamcorper. Mauris leo. Curabit feugiat lectus vestibulum tincidunt enim. Cras eget augue. Pellentesque varius nec, scelerisque odio neque, eu auctor tincidunt. Sed</p>
  </div>

  <div class="signature">Signature</div>

  <footer class="letter-footer">
    <div class="company-line">Q Ventures for rental tools and equipment</div>
    <div class="address-line">5, 12th floor, amber crest tower, Marlow Quay, Abu Dhabi</div>
    <div class="contact-grid">
      <div class="contact-item">
        <svg viewBox="0 0 10 10" aria-hidden="true"><path d="M2 0.5 L3.8 2.6 L2.9 3.7 C3.5 5 4.9 6.4 6.3 7.1 L7.4 6.2 L9.5 8 L8.3 9.5 C4.5 9.2 0.8 5.5 0.5 1.7 Z"/></svg>
        <span>02-418 5927</span>
      </div>
      <div class="contact-item">
        <svg viewBox="0 0 10 10" aria-hidden="true"><path d="M5 0 L9.5 0 L9.5 0.5 Z M2.5 0 H7.5 V10 H2.5 Z M3.3 1 V8 H6.7 V1 Z"/></svg>
        <span>info@qventures.com</span>
      </div>
      <div class="contact-item">
        <svg viewBox="0 0 10 10" aria-hidden="true"><path d="M2.5 0 H7.5 V10 H2.5 Z M3.3 1 V8 H6.7 V1 Z"/></svg>
        <span>050 847 3062</span>
      </div>
      <div class="contact-item">
        <svg viewBox="0 0 10 10" aria-hidden="true"><circle cx="5" cy="5" r="5"/></svg>
        <span>www.qventures.com</span>
      </div>
    </div>
  </footer>
</section>

<section class="sheet envelope-back">
  <svg class="envelope-flap" viewBox="0 0 450 49" preserveAspectRatio="none" aria-hidden="true">
    <path d="M0 0 H450 L442 38 Q440 49 428 49 H22 Q10 49 8 38 Z" fill="#0d56a6"/>
  </svg>
  <div class="brand-mark"><span class="brand-dot"></span>Q VENTURES</div>
</section>

<section class="sheet envelope-front">
  <div class="side-band"></div>
  <div class="brand-mark"><span class="brand-dot"></span>Q VENTURES</div>
  <div class="envelope-address">5, 12th floor, amber crest tower,<br>Marlow Quay, Abu Dhabi</div>
</section>

</body>
</html>
```